Business card design needed

We are a boutique law firm within the Melbourne CBD.

You will need to upload our company logo which is to go on the left hand side of the business card - we then have a Bar Collegium of Tarnwell logo to go perhaps on the bottom right hand side (color)

On the back we would like the website details

www.marlowessolicitors.com.au - with a small logo
Updates

Thank you designers for all your great submissions.  Just going through the designs and we will choose one within the next couple of days.

Kind Regards
Marlowes Solicitors Pty Ltd

Industry/Entity Type

Boutique

Contact Information for Business Card

Dermot Marlowe
Principal
Level 6, 47 Quarry Lane
Melbourne VIC Australia 3000
T+61 3 9620 2088 F+61 3 9629 3938
dermot@marlowessolicitors.com.au
M 0491 570 156

```html
<!DOCTYPE html>
<html lang="en">
<head>
<meta charset="utf-8">
<title>Marlowes Solicitors — Business Card</title>
<link rel="stylesheet" href="https://fonts.googleapis.com/css2?family=Roboto+Condensed:wght@400;700&family=Alegreya:wght@400;700&display=swap">
<style>
  :root {
    --backdrop: #9a9a98;
    --card-dark: #1c1c1c;
    --card-dark-edge: #2b2b2b;
    --card-light: #f2f2f0;
    --ink-dark: #1e1e1e;
    --ink-light: #e6e6e4;
    --rule: #1e1e1e;
  }
  * { margin: 0; padding: 0; box-sizing: border-box; }
  html, body {
    width: 1200px; height: 944px; overflow: hidden;
    background: var(--backdrop);
  }
  .sheet {
    width: 1200px; height: 944px;
    display: flex; flex-direction: column;
    align-items: center; justify-content: center; gap: 40px;
  }
  .card {
    width: 640px; height: 391px;
    position: relative;
    box-shadow: 0 6px 18px rgba(0,0,0,0.25);
  }
  .card--back {
    background: radial-gradient(circle at 50% 40%, var(--card-dark-edge), var(--card-dark) 70%);
    display: flex; flex-direction: column; align-items: center; justify-content: center;
    color: var(--ink-light);
  }
  .card--front { background: var(--card-light); color: var(--ink-dark); }

  .brand {
    display: flex; align-items: center; gap: 12px;
    font-family: "Roboto Condensed", sans-serif;
    font-weight: 700; font-size: 52px; letter-spacing: -1px; line-height: 1;
  }
  .brand__mark { width: 40px; height: 40px; background: currentColor; }
  .web {
    font-family: "Roboto Condensed", sans-serif;
    font-weight: 400; font-size: 15px; letter-spacing: 4.2px;
    text-transform: uppercase; margin-top: 14px;
  }

  .front__identity {
    position: absolute; left: 44px; top: 130px; width: 290px;
  }
  .front__identity .brand { font-size: 46px; }
  .front__identity .brand__mark { width: 34px; height: 34px; }
  .front__identity .web { font-size: 13px; letter-spacing: 3.2px; }

  .front__rule {
    position: absolute; left: 350px; top: 60px; width: 3px; height: 270px;
    background: var(--rule);
  }
  .contact {
    position: absolute; left: 372px; top: 68px; width: 250px;
    font-family: "Alegreya", serif; font-size: 15px; line-height: 1.3;
  }
  .contact__name { font-weight: 700; }
  .contact__block { margin-top: 14px; }
  .contact__block:first-child { margin-top: 0; }
</style>
</head>
<body>
<main class="sheet">
  <section class="card card--back" aria-label="Card back">
    <div class="brand"><span class="brand__mark"></span><span>Marlowes</span></div>
    <p class="web">www.marlowessolicitors.com.au</p>
  </section>

  <section class="card card--front" aria-label="Card front">
    <div class="front__identity">
      <div class="brand"><span class="brand__mark"></span><span>Marlowes</span></div>
      <p class="web">www.marlowessolicitors.com.au</p>
    </div>
    <div class="front__rule"></div>
    <div class="contact">
      <div class="contact__block">
        <p class="contact__name">Dermot Marlowe Principal Marlowes Solicitors Pty Ltd</p>
        <p>Level 6, 47 Quarry Lane,</p>
        <p>Melbourne VIC Australia 3000</p>
      </div>
      <div class="contact__block">
        <p>T+61 3 9555 0147, F+61 3 9555 0382</p>
      </div>
      <div class="contact__block">
        <p>dermot@marlowessolicitors.com.au</p>
        <p>M 0491 570 156</p>
      </div>
    </div>
  </section>
</main>
</body>
</html>
```